Webpage Wordpress Redesign

Need a redesign of a current wordpress. Project did not meet needed requirements and formatting was never completed. Functionality is fairly close to where it should be but need some help to make it usable.

Current site - http://brightmarsh.org

As you can see images are not visible any longer for some reason. Needs to have a clean simple layout with the ability to receive donations through paynest.

Requirements
Must have
• Needs to be able to have picture functionality. Needs to have a usable email sign-up collection option, even if that means using the form created through mailchimp or something. Need to have a blog like page for easy update of new articles and information. Needs to have a clean simple layout with the ability to receive donations through paynest.

```html
<!DOCTYPE html>
<html lang="en">
<head>
<meta charset="utf-8">
<title>Brightmarsh Life League</title>
<link href="https://fonts.googleapis.com/css2?family=Sorts+Mill+Goudy&family=Open+Sans:ital,wght@0,400;0,600;0,700;1,600&family=Arimo:wght@400;700&display=swap" rel="stylesheet">
<style>
:root{
  --page:#e9ecef;
  --pink:#e06a9e;
  --pink-deep:#c8306e;
  --brand:#d83a7c;
  --blue:#3f87c9;
  --steel:#93a9c2;
  --slide:#e2e0dd;
  --ink:#333;
  --muted:#555;
  --footer:#d9dfe6;
  --heading-blue:#4aa3de;
}
*{box-sizing:border-box;margin:0;padding:0}
html,body{width:1104px;height:1200px;overflow:hidden}
body{background:var(--page);font-family:"Open Sans",sans-serif;color:var(--ink);position:relative}
.site-title{position:absolute;right:134px;top:24px;text-align:right;font-family:"Sorts Mill Goudy",serif;color:var(--brand)}
.site-title h1{font-weight:400;font-size:36px;line-height:40px}
.site-title p{font-size:14px;margin-top:2px}
.nav-band{position:absolute;left:0;top:119px;width:1104px;height:34px;background:var(--pink)}
.nav-tab{position:absolute;top:122px;height:31px;font-family:"Sorts Mill Goudy",serif;font-size:15px;line-height:31px;text-align:center;color:#222;background:var(--pink-deep)}
.nav-tab.active{background:#fff;color:#333}
.content{position:absolute;left:93px;top:172px;width:767px;height:713px;border:1px solid #dcdfe3;background:rgba(240,242,244,.5)}
.slider{position:absolute;left:93px;top:198px;width:762px;height:329px;background:var(--slide);border-top:2px solid #f2f2f2}
.slide-title{position:absolute;left:170px;top:253px;font-family:"Arimo",sans-serif;font-weight:700;font-size:50px;color:#fff;white-space:nowrap;letter-spacing:-.5px}
.slide-photo{position:absolute;left:557px;top:268px;width:237px;height:114px;background:linear-gradient(135deg,#8a7a70,#3d3a44 55%,#6d5a57)}
.slide-text{position:absolute;left:170px;top:326px;width:330px;font-family:"Arimo",sans-serif;font-style:italic;font-size:14px;line-height:21px;color:#666}
.read-more{position:absolute;left:170px;top:443px;width:108px;height:36px;border:5px solid #fff;border-radius:20px;background:#d8d6d3;font-family:"Sorts Mill Goudy",serif;font-size:12px;font-weight:700;line-height:26px;text-align:center;color:#555}
.dots{position:absolute;left:454px;top:488px;display:flex;gap:4px}
.dots span{width:9px;height:9px;border-radius:50%;background:#999}
.dots span.on{background:#fff;border:1px solid #999}
.section-title{position:absolute;left:103px;top:553px;font-family:"Sorts Mill Goudy",serif;font-weight:400;font-size:27px;color:var(--blue)}
.rule{position:absolute;left:93px;top:594px;width:762px;height:1px;background:#ccc}
.quote{position:absolute;top:606px;width:240px;font-size:11px;line-height:17.5px;font-weight:600;color:#555}
.quote cite{display:block;margin-top:16px;font-style:italic}
.steel-bar{position:absolute;left:93px;top:811px;width:760px;height:10px;background:var(--steel)}
.yellow-line{position:absolute;left:93px;top:830px;width:760px;height:1px;background:#f2f25a}
.donate{position:absolute;left:102px;top:843px;font-family:"Sorts Mill Goudy",serif;font-size:11px;color:#444}
.sidebar-title{position:absolute;left:874px;top:170px;font-family:"Sorts Mill Goudy",serif;font-size:24px;color:#111}
.side-link{position:absolute;left:870px;width:147px;height:21px;font-family:"Sorts Mill Goudy",serif;font-size:14px;line-height:21px;padding-left:4px;color:var(--blue)}
.side-link.active{background:#b9d3ec;border-radius:3px}
.footer{position:absolute;left:0;top:893px;width:1104px;height:307px;background:var(--footer)}
.tagline{position:absolute;left:96px;top:924px;width:227px;height:187px;background:var(--steel);padding:6px 8px;font-family:"Arimo",sans-serif;font-weight:700;font-size:28px;line-height:25px;color:#fff}
.foot-head{position:absolute;top:922px;font-family:"Arimo",sans-serif;font-weight:700;font-size:17px;color:var(--heading-blue)}
.social{position:absolute;left:359px;width:158px;height:53px;background:#fff;border:1px solid #aab;display:flex;align-items:center;gap:8px;padding-left:10px;font-family:"Arimo",sans-serif;font-weight:700;font-size:15px;color:#2b6cb0}
.social i{width:20px;height:20px;background:#2b6cb0;border-radius:3px;flex:none}
.contact{position:absolute;left:559px;display:flex;align-items:center;gap:5px;font-family:"Arimo",sans-serif;font-weight:700;font-size:11px;color:#222}
.contact svg{width:13px;height:13px}
.form-label{position:absolute;font-family:"Sorts Mill Goudy",serif;font-size:10px;color:#333}
.field{position:absolute;background:#eef1f4;border:1px solid #999}
.submit{position:absolute;left:874px;top:1095px;width:43px;height:16px;background:#f4f4f4;border:1px solid #999;font-family:"Sorts Mill Goudy",serif;font-size:11px;line-height:14px;text-align:center}
.copyright{position:absolute;left:0;width:1104px;top:1129px;text-align:center;font-family:"Sorts Mill Goudy",serif;font-size:10px;color:#333}
</style>
</head>
<body>
<header class="site-title">
  <h1>Brightmarsh Life League</h1>
  <p>Defending Human Innocent Life Since 1971</p>
</header>

<nav>
  <div class="nav-band"></div>
  <a class="nav-tab active" style="left:655px;width:77px">Home</a>
  <a class="nav-tab" style="left:741px;width:81px">About</a>
  <a class="nav-tab" style="left:831px;width:81px">News</a>
  <a class="nav-tab" style="left:921px;width:92px">Contact</a>
</nav>

<main>
  <div class="content"></div>
  <section class="slider"></section>
  <div class="slide-photo" role="img" aria-label="News photo of officials at a press event"></div>
  <h2 class="slide-title">Judge Rules Morning ...</h2>
  <p class="slide-text">&nbsp;&nbsp;As a pro-life organization we are extremely disappointed by the ruling sent down from U.S. District Judge Edward Lowell. A judge has now forced offering of an abortive substance to minors</p>
  <div class="read-more">Read more</div>
  <div class="dots"><span></span><span class="on"></span><span></span></div>

  <h2 class="section-title">What Is Life</h2>
  <div class="rule"></div>
  <blockquote class="quote" style="left:103px">“We must not be surprised when we hear of murders, killings, of wars, or of hatred.  If a mother can kill her own child, what is left but for us to kill each other? ”<cite>Margaret Hale</cite></blockquote>
  <blockquote class="quote" style="left:353px">“America you are beautiful . . . and blessed . . . The ultimate test of your greatness is the way you treat every human being, but especially the weakest and most defenseless. If you want equal justice for all and true freedom and lasting peace, then America, defend life.”<cite>Thomas Alden</cite></blockquote>
  <blockquote class="quote" style="left:611px;width:230px">“Sweeter even than to have had the joy of caring for children of my own has it been to me to help bring about a better state of things for mothers generally, so their unborn little ones could not be willed away from them.”<cite>Eleanor Price 1889</cite></blockquote>

  <div class="steel-bar"></div>
  <div class="yellow-line"></div>
  <p class="donate">[incert paynest donation here]</p>
</main>

<aside>
  <h3 class="sidebar-title">Vertical Menu</h3>
  <a class="side-link active" style="top:204px">‹ Home</a>
  <a class="side-link" style="top:227px">‹ About</a>
  <a class="side-link" style="top:251px">‹ News</a>
  <a class="side-link" style="top:275px">‹ Contact</a>
</aside>

<footer>
  <div class="footer"></div>
  <div class="tagline">LIFE:<br>BECAUSE<br>EVERY<br>LIFE IS<br>WORTH<br>LIVING</div>

  <h4 class="foot-head" style="left:374px">SOCIAL MEDIA</h4>
  <div class="social" style="top:952px"><i></i>Follow on Chirpline</div>
  <div class="social" style="top:1031px"><i></i>Find us on Friendbook</div>

  <h4 class="foot-head" style="left:561px">BRIGHTMARSH LIFE LEAGUE</h4>
  <div class="contact" style="top:960px"><svg viewBox="0 0 14 14"><circle cx="7" cy="7" r="7" fill="#d83a7c"/><path d="M4 3.5l2 .2.5 2-1 .8a6 6 0 0 0 2.5 2.5l.8-1 2 .5.2 2c-4 .5-7.5-3-7-7z" fill="#222"/></svg>855-555-0142</div>
  <div class="contact" style="top:984px"><svg viewBox="0 0 14 14"><circle cx="7" cy="7" r="7" fill="#d83a7c"/><rect x="3.5" y="4.5" width="7" height="5" fill="#fff"/><path d="M3.5 4.5 7 7.5 10.5 4.5" stroke="#222" fill="none"/></svg>hello@brightmarsh.org</div>
  <div class="contact" style="top:1009px"><svg viewBox="0 0 14 14"><circle cx="7" cy="7" r="7" fill="#d83a7c"/><path d="M3 7.5 7 3.5l4 4H10v3H4v-3z" fill="#fff"/></svg>Marshfield, FL</div>
  <div class="contact" style="top:1036px"><svg viewBox="0 0 14 14"><circle cx="7" cy="7" r="7" fill="#d83a7c"/><circle cx="7" cy="5.5" r="2" fill="#222"/><path d="M3.5 11a3.5 3 0 0 1 7 0z" fill="#222"/></svg>Dana Whitfield, Executive Director</div>

  <h4 class="foot-head" style="left:821px">SEND US A NOTE</h4>
  <span class="form-label" style="left:799px;top:966px">Name:</span>
  <div class="field" style="left:829px;top:961px;width:150px;height:24px"></div>
  <span class="form-label" style="left:801px;top:991px;text-decoration:underline">Email:</span>
  <div class="field" style="left:829px;top:986px;width:150px;height:24px"></div>
  <div class="field" style="left:810px;top:1011px;width:172px;height:82px"></div>
  <div class="submit">Submit</div>

  <p class="copyright">Copyright © 2011 All Rights Reserved.</p>
</footer>
</body>
</html>
```